In Home Personal IT Consultant (Nerd) Website and Logo QTgeek.net

Website and logo design for in home personal "nerd". Consulting services provided: Home Automation, Home Theater, Network and Wi-Fi installation, Computer Repair, and Virus Removal. Need simple site to promote QTgeek.net based in Santa Fe, New Mexico. You may choose to incorporate the Zia symbol from the New Mexico flag into the design, not mandatory. I am also a big fan of the movie Return of the Tinkers.
I have over 10 years of experience in the hospitality industry working with multi million dollar hotels and will apply that same level of service to the home. TechVara B+ and Shieldwise+ Certified. Available by appointment, primarily Evenings and Weekends. Consulting rate will be $70/hr.
Industry/Entity Type
Consulting
Number of Pages Required
1 page
Look and feel
Each slider illustrates characteristics of the customer's brand and the style your logo design should communicate.

```html
<!DOCTYPE html>
<html lang="en">
<head>
<meta charset="UTF-8">
<title>Why QT geek?</title>
<link href="https://fonts.googleapis.com/css2?family=Source+Sans+3:wght@600;700&display=swap" rel="stylesheet">
<style>
  :root {
    --bg-deep: #042830;
    --bg-mid: #0a3238;
    --bg-light: #14393c;
    --heading: #ffffff;
    --rule: #a9abad;
    --bubble: #ffffff;
    --quote-ink: #0e2433;
  }
  * { margin: 0; padding: 0; box-sizing: border-box; }
  html, body {
    width: 1200px;
    height: 700px;
    overflow: hidden;
    background: var(--bg-deep);
  }
  .testimonials {
    position: relative;
    width: 1200px;
    height: 700px;
    overflow: hidden;
    font-family: "Source Sans 3", "Myriad Pro", Arial, sans-serif;
  }
  .testimonials__backdrop {
    position: absolute;
    inset: 0;
    background:
      radial-gradient(ellipse 700px 420px at 900px 520px, var(--bg-light) 0%, rgba(20,57,60,0) 70%),
      linear-gradient(160deg, var(--bg-deep) 0%, var(--bg-mid) 60%, var(--bg-deep) 100%);
  }
  .testimonials__title {
    position: absolute;
    top: 42px;
    left: 0;
    width: 100%;
    text-align: center;
    color: var(--heading);
    font-weight: 700;
    font-size: 27px;
    letter-spacing: 0.2px;
  }
  .testimonials__rule {
    position: absolute;
    top: 91px;
    left: 447px;
    width: 303px;
    height: 8px;
    border-radius: 4px;
    background: var(--rule);
  }
  .quote-bubble {
    position: absolute;
    width: 508px;
    height: 166px;
  }
  .quote-bubble__shape {
    position: absolute;
    inset: 0;
    width: 100%;
    height: 100%;
    fill: var(--bubble);
  }
  .quote-bubble__body {
    position: absolute;
    top: 13px;
    left: 30px;
    right: 30px;
    color: var(--quote-ink);
    font-weight: 600;
    font-size: 16.6px;
    line-height: 22px;
  }
  .quote-bubble__author {
    display: block;
    text-align: right;
    margin-top: 5px;
    font-style: normal;
  }
  .quote-bubble--first  { top: 152px; left: 119px; }
  .quote-bubble--second { top: 318px; left: 571px; }
  .quote-bubble--third  { top: 485px; left: 119px; }
  .quote-bubble--second .quote-bubble__body { left: 37px; right: 32px; }
</style>
</head>
<body>
  <section class="testimonials">
    <div class="testimonials__backdrop" role="img" aria-label="Dark teal close-up photograph of a laptop keyboard"></div>

    <h1 class="testimonials__title">Why QT geek?</h1>
    <div class="testimonials__rule"></div>

    <figure class="quote-bubble quote-bubble--first">
      <svg class="quote-bubble__shape" viewBox="0 0 508 166" aria-hidden="true">
        <path d="M0,30 Q0,0 30,0 H478 Q508,0 508,30 V80 Q508,110 478,110 H90 Q22,112 0,166 Z"/>
      </svg>
      <blockquote class="quote-bubble__body">
        “Lorem ipsum dolor sit amet, consectetuer adipiscing<br>
        elit. Aenean commodo ligula eget dolor. Aenean massa.<br>
        Cum sociis parturient montes, nascetur ridiculus mus.”
        <cite class="quote-bubble__author">-John Doe</cite>
      </blockquote>
    </figure>

    <figure class="quote-bubble quote-bubble--second">
      <svg class="quote-bubble__shape" viewBox="0 0 508 166" aria-hidden="true">
        <path d="M508,30 Q508,0 478,0 H30 Q0,0 0,30 V80 Q0,110 30,110 H418 Q486,112 508,166 Z"/>
      </svg>
      <blockquote class="quote-bubble__body">
        “ Nullam quis ante. Etiam sit amet orci eget eros faucibus<br>
        tincidunt. Duis leo. Sed fringilla mauris sit amet nibh.<br>
        Donec sodales sagittis magna.”
        <cite class="quote-bubble__author">-Jane Doe</cite>
      </blockquote>
    </figure>

    <figure class="quote-bubble quote-bubble--third">
      <svg class="quote-bubble__shape" viewBox="0 0 508 166" aria-hidden="true">
        <path d="M0,30 Q0,0 30,0 H478 Q508,0 508,30 V80 Q508,110 478,110 H90 Q22,112 0,166 Z"/>
      </svg>
      <blockquote class="quote-bubble__body">
        “Lorem ipsum dolor sit amet, consectetuer adipiscing<br>
        elit. Aenean commodo ligula eget dolor. Aenean massa.<br>
        Cum sociis parturient montes, nascetur ridiculus mus.”
        <cite class="quote-bubble__author">-John Doe</cite>
      </blockquote>
    </figure>
  </section>
</body>
</html>
```